Need Label for Our Jams Product

HI,

we have are launching a new brand in the premium foods category by the name of Vo-Marta. the logo has been designed and our first product is Premium 65% fruit Jams. we need a label for it now. can you help ?

our flavours are strawberry, apple, mango, blackberry, cherry, PineApple.

Please note that we need one design and then we will modify it according to the flavour. so you will need to make one flavour on a theme. and then we will apply the theme accordingly to the rest of the flavours.

Target Market(s)

Health concious people who donot want to use ordinary jams any further.

Industry/Entity Type

Product

Requirements
Must have
• the logo, not too big because we need the flavour name aswell on the front of the label.
also would appreciate a touch of fruit or similar
also please note that the colour of the cap in the attached picture is the actual colour. and the label should incline with the colour of cap aswell. im not saying the label to be in that colour, but must balance the whole look of the bottle.
Please note that this is a round bottle, so much information is needed on the front. the sides of the labels will be occupied by ingredients nutrition facts etc.
Nice to have
• white background but not necessary.
Should not have
• black colour

```html
<!DOCTYPE html>
<html lang="en">
<head>
<meta charset="utf-8">
<title>Vo-Marta Strawberry Jam Label</title>
<link rel="stylesheet" href="https://fonts.googleapis.com/css2?family=Alfa+Slab+One&display=swap">
<style>
  :root {
    --page: #f1efec;
    --label: #ffffff;
    --berry: #9a1c6c;
    --gold: #e3a21f;
  }
  * { margin: 0; padding: 0; box-sizing: border-box; }
  html, body {
    width: 945px;
    height: 1200px;
    overflow: hidden;
    background: var(--page);
  }
  .canvas {
    position: relative;
    width: 945px;
    height: 1200px;
  }
  .label {
    position: absolute;
    left: 32px;
    top: 370px;
    width: 880px;
    height: 460px;
    background: var(--label);
    overflow: hidden;
  }
  .stripe {
    position: absolute;
    top: 0;
    bottom: 0;
  }
  .stripe--berry { left: 0; width: 20px; background: var(--berry); }
  .stripe--gold { left: 38px; width: 12px; background: var(--gold); }
  .brand {
    position: absolute;
    left: 120px;
    top: 28px;
    font-family: "Alfa Slab One", serif;
    font-size: 28px;
    line-height: 34px;
    color: var(--berry);
  }
  .flavour {
    position: absolute;
    left: 110px;
    top: 78px;
    font-family: "Alfa Slab One", serif;
    font-weight: 400;
    font-size: 168px;
    line-height: 164px;
    letter-spacing: 6px;
    color: var(--berry);
  }
  .flavour span { display: block; }
</style>
</head>
<body>
  <main class="canvas">
    <section class="label">
      <div class="stripe stripe--berry"></div>
      <div class="stripe stripe--gold"></div>
      <div class="brand">Vo-Marta</div>
      <h1 class="flavour"><span>straw</span><span>berry</span></h1>
    </section>
  </main>
</body>
</html>
```